From Portrait to Landscape

Take a PPT document made of 54 slide of graphs, images and text and change the orientation of each one of the 54 slides from the existing Portrait layout to the Landscape one.
All the graphics and texts (including text formatting, commas, bullet points etc.) must be kept the same but spaces are reorganized in the new Landscape orientation favoring the size of the graphs (possibily reducing the text areas).
Please, find attached the first 10 pages of the PPT document (for now, in PDF format) and a couple of sample pages of the PPT.x\

Target Market(s)

Readers of the Report (ecommerce players in Italy)

Requirements
Must have
• Graphics should be larger in the Landscape orientation than they are now in the Poirtrait one

```html
<!DOCTYPE html>
<html lang="it">
<head>
<meta charset="utf-8">
<title>L'ecommerce in Italia – Dimensioni e trend</title>
<link rel="stylesheet" href="https://fonts.googleapis.com/css2?family=Carlito:wght@400;700&family=Open+Sans:wght@400;700&display=swap">
<style>
  :root {
    --green: #6f8a3c;
    --band: #738446;
    --row-grey: #cdcdcd;
    --ink: #262626;
    --head-grey: #8a8a8a;
    --note-grey: #9a9a9a;
    --paper: #ffffff;
  }
  * { margin: 0; padding: 0; box-sizing: border-box; }
  html, body { width: 1200px; height: 892px; overflow: hidden; background: var(--paper); }
  .slide { position: relative; width: 1200px; height: 892px; font-family: "Carlito", "Calibri", sans-serif; color: var(--ink); }

  .slide-title {
    position: absolute; left: 84px; top: 52px;
    font-family: "Open Sans", sans-serif; font-weight: 700; font-size: 24px;
    letter-spacing: 2.2px; color: var(--green);
  }
  .title-rule { position: absolute; left: 82px; top: 81px; width: 367px; height: 2px; background: var(--green); }
  .slide-subtitle {
    position: absolute; left: 84px; top: 88px;
    font-size: 29px; color: var(--green); letter-spacing: -0.3px;
  }

  .kpi-table { position: absolute; left: 84px; top: 130px; width: 1031px; border-collapse: collapse; }
  .kpi-table th {
    font-weight: 700; font-size: 17px; color: var(--head-grey);
    height: 53px; vertical-align: middle; line-height: 1.3;
    border-bottom: 1px solid #333;
  }
  .kpi-table th.col-label { text-align: left; padding-left: 9px; }
  .kpi-table td { height: 38px; font-size: 15.5px; vertical-align: middle; }
  .kpi-table td.col-label { width: 599px; padding-left: 9px; }
  .kpi-table td.col-value { width: 210px; text-align: center; }
  .kpi-table td.col-delta { text-align: center; }
  .kpi-table tbody tr:nth-child(odd) td { background: var(--row-grey); }
  .kpi-table tbody tr:nth-child(odd) td.col-label { border-right: 1px solid #e4e4e4; }

  .footnotes { position: absolute; right: 85px; top: 770px; text-align: right; font-size: 18.5px; color: var(--note-grey); line-height: 31px; }

  .footer-band {
    position: absolute; left: 53px; top: 840px; width: 1100px; height: 27px;
    border-radius: 14px; background: var(--band); color: #fff;
    font-family: "Open Sans", sans-serif; font-size: 15px;
    display: flex; justify-content: space-between; align-items: center;
    padding: 0 37px 0 34px;
  }
</style>
</head>
<body>
<main class="slide">
  <h1 class="slide-title">L’ECOMMERCE IN ITALIA</h1>
  <div class="title-rule"></div>
  <h2 class="slide-subtitle">Dimensioni e trend</h2>

  <table class="kpi-table">
    <thead>
      <tr>
        <th class="col-label">Indicatore</th>
        <th class="col-value">Valore</th>
        <th class="col-delta">Variaz pre<br>pandemia</th>
      </tr>
    </thead>
    <tbody>
      <tr><td class="col-label">Utenti Internet in Italia 15+ (settimanali)</td><td class="col-value">42,5 milioni</td><td class="col-delta">+9,6%</td></tr>
      <tr><td class="col-label">Acquirenti online tra utenti Internet</td><td class="col-value">77,8%</td><td class="col-delta">+16,9 p.p.</td></tr>
      <tr><td class="col-label">Acquirenti online nel trimestre</td><td class="col-value">33,3 milioni</td><td class="col-delta">+40,2%</td></tr>
      <tr><td class="col-label">Acquirenti online abituali (una volta al mese)</td><td class="col-value">23,9 milioni</td><td class="col-delta">+44,7%</td></tr>
      <tr><td class="col-label">Acquirenti online ogni 100 abitanti 18+</td><td class="col-value">66,0</td><td class="col-delta">+40,2%</td></tr>
      <tr><td class="col-label">Quota di acquirenti online uomini</td><td class="col-value">51,9%</td><td class="col-delta">-0,6 p.p.</td></tr>
      <tr><td class="col-label">Età media degli acquirenti online</td><td class="col-value">42,2 anni</td><td class="col-delta">- 0,8 anni</td></tr>
      <tr><td class="col-label">Acquisti online nel trimestre</td><td class="col-value">127,9 milioni</td><td class="col-delta">+45,7%</td></tr>
      <tr><td class="col-label">Quota acquisti online da dispositivi mobili</td><td class="col-value">55,6%</td><td class="col-delta">+10,2 p.p.</td></tr>
      <tr><td class="col-label">Quota acquirenti online via App nel semestre</td><td class="col-value">57,2%</td><td class="col-delta">+13,5 p.p.</td></tr>
      <tr><td class="col-label">Valore mensile acquisti online nel 2021</td><td class="col-value">4.950 Mio €</td><td class="col-delta">+33,1%</td></tr>
      <tr><td class="col-label">Quota a valore degli acquisti di prodotti</td><td class="col-value">73,9%</td><td class="col-delta">+ 20,8 p.p.</td></tr>
      <tr><td class="col-label">Media acquisti online pro-capite nel trimestre</td><td class="col-value">3,83</td><td class="col-delta">+ 3,9% Y/Y</td></tr>
      <tr><td class="col-label">Valore acquisti online nel 2021</td><td class="col-value">51,8 B€</td><td class="col-delta">+36,3% Y/Y</td></tr>
      <tr><td class="col-label">Previsione valore acquisti online nel 2022</td><td class="col-value">56,4 B€</td><td class="col-delta">+8,9% Y/Y</td></tr>
    </tbody>
  </table>

  <div class="footnotes">
    <p>Gli indicatori – se non diversamente indicato - si riferiscono al mese medio del primo trimestre 2022</p>
    <p>La differenza rispetto al periodo pre-pandemico confronta i dati del 2019 con quelli del 2022</p>
  </div>

  <footer class="footer-band">
    <span>Shop Digitale – Aprile 2022</span>
    <span>5</span>
  </footer>
</main>
</body>
</html>
```